Urgent - brand new business card for a startup technical advisory and incubation business in Sydney

We need a brand new business card design for BrightForge. We are a startup technical advisory and incubation business based in Sydney Australia. We work with entrepreneurs and innovators to help rapidly and efficiently turn their ideas into reality and to ensure they have the technical platform required for growth.

Our name is partly inspired by our love of lean product development methods and the lean startup movement.

We would like clean, uncluttered designs that feature our two logo colours and communicate a professional but creative, in-touch and entrepreneurial business.

PLEASE SEE MUST HAVE PRIORITIES FOR DRAFT CONTACT INFORMATION AND OTHER DESIRED TEXT ON CARD.
Updates

We have now updated the brief to include draft business card contact information and also some additional desired text to feature on the card design.    Please review the Must Have priorities.

Also final updated source files for the horizontal and vertical versions have now been uploaded and should be used for any designs.

Thanks!

Target Market(s)

Entrepeneurs, innovators, startup investors looking for a strong product development partner

Industry/Entity Type

Business

Requirements
Must have
• Feature our two logo colours
Be a relatively clean, pared back overall design - quite minimalist

Updated source files (AI) for vertical and horizontal layouts attached.

Draft contact information for business card:
Neil Barton
Founder & CTO
Phone: +61 427 555123
Email: xxxx@brightforge.com
Skype: xxxxxbarton
Twitter: nbarton

www.brightforge.com

We would also like the overall design to include the phrase "You have great ideas. Let us make them happen." (probably in a reasonably subtle way)

Nice to have
• Inspire me! Double-sided designs are fine with logo, phrase, (URL?) on one side and contact details on other (+ any other design elements)

Logo on business card can be either with lightbulb above the wording as per example here or to the left of the BrightForge wording - both layouts in files provided.
Should not have
• Shouldn't look like a Pentara Suite business card template :-)

```html
<!DOCTYPE html>
<html lang="en">
<head>
<meta charset="utf-8">
<title>BrightForge Business Card</title>
<link href="https://fonts.googleapis.com/css2?family=PT+Sans:wght@400;700&display=swap" rel="stylesheet">
<style>
  :root {
    --stage: #4b4a4f;
    --card-light-center: #d4ecfa;
    --card-light-edge: #a9b8c2;
    --card-dark: #121d22;
    --brand-blue: #1fa9e4;
    --brand-ink: #1b2329;
    --silver-light: #e4e8ea;
    --silver-mid: #b9c3c9;
    --silver-dark: #5f6f78;
    --white: #ffffff;
  }
  * { margin: 0; padding: 0; box-sizing: border-box; }
  html, body { width: 1200px; height: 1000px; overflow: hidden; }
  body {
    background: var(--stage);
    font-family: "PT Sans", "Myriad Pro", sans-serif;
    position: relative;
  }

  /* Front card */
  .card-front {
    position: absolute; left: 195px; top: 128px; width: 598px; height: 342px;
    background: radial-gradient(ellipse 60% 70% at 50% 42%, var(--card-light-center), var(--card-light-edge));
    overflow: hidden;
  }
  .card-front .silver-rule {
    position: absolute; left: 0; top: 292px; width: 100%; height: 8px;
    background: linear-gradient(to bottom, var(--silver-light), var(--silver-mid));
  }
  .card-front .dark-band {
    position: absolute; left: 0; top: 300px; width: 100%; height: 42px;
    background: var(--card-dark);
  }
  .brand-lockup {
    position: absolute; display: flex; align-items: center;
  }
  .brand-lockup .brand-dot {
    border-radius: 50%; background: var(--brand-blue); flex: none;
  }
  .brand-lockup .brand-name {
    font-weight: 700; color: var(--brand-blue); letter-spacing: -0.5px; line-height: 1;
  }
  .card-front .brand-lockup { left: 150px; top: 128px; gap: 22px; }
  .card-front .brand-dot { width: 70px; height: 70px; }
  .card-front .brand-name { font-size: 56px; }

  /* Back card */
  .card-back {
    position: absolute; left: 407px; top: 493px; width: 598px; height: 342px;
    background: var(--card-dark); overflow: hidden;
  }
  .card-back .metal-strip {
    position: absolute; left: 0; width: 100%; height: 7px;
    background: linear-gradient(to right, var(--silver-dark), var(--silver-mid) 50%, var(--silver-dark));
  }
  .card-back .metal-strip.top { top: 0; }
  .card-back .metal-strip.bottom { bottom: 0; }
  .logo-panel {
    position: absolute; left: 0; top: 87px; width: 266px; height: 185px;
    background: linear-gradient(to right, var(--silver-mid), var(--silver-light) 55%, var(--silver-mid));
    border-radius: 0 20px 20px 0;
  }
  .logo-panel .brand-lockup {
    left: 0; top: 30px; width: 266px; flex-direction: column; gap: 28px;
  }
  .logo-panel .brand-dot { width: 62px; height: 62px; }
  .logo-panel .brand-name { font-size: 36px; }

  .identity { position: absolute; left: 309px; top: 84px; color: var(--white); }
  .identity .person-name { font-size: 33px; font-weight: 700; line-height: 1.1; }
  .identity .person-role { font-size: 19px; font-weight: 400; line-height: 1.2; }

  .contact-list {
    position: absolute; left: 328px; top: 167px; list-style: none;
  }
  .contact-list li {
    display: flex; align-items: center; height: 25.5px;
    color: var(--brand-blue); font-size: 15.5px;
  }
  .contact-list svg { width: 22px; height: 22px; margin-right: 11px; flex: none; }
</style>
</head>
<body>

  <section class="card-front" aria-label="Card front">
    <div class="brand-lockup">
      <span class="brand-dot"></span>
      <span class="brand-name">BrightForge</span>
    </div>
    <div class="silver-rule"></div>
    <div class="dark-band"></div>
  </section>

  <section class="card-back" aria-label="Card back">
    <div class="metal-strip top"></div>
    <div class="logo-panel">
      <div class="brand-lockup">
        <span class="brand-dot"></span>
        <span class="brand-name">BrightForge</span>
      </div>
    </div>

    <div class="identity">
      <h1 class="person-name">Neil Barton</h1>
      <p class="person-role">Founder and CTO</p>
    </div>

    <ul class="contact-list">
      <li>
        <svg viewBox="0 0 22 22" aria-hidden="true">
          <circle cx="11" cy="11" r="9.5" fill="none" stroke="var(--brand-blue)" stroke-width="1.6"/>
          <path d="M7.5 6.5 L9.3 6.2 L10.2 8.6 L9 9.5 Q10 12 12.5 13 L13.4 11.8 L15.8 12.7 L15.5 14.5 Q11 15.5 8 12 Q6.3 9.5 7.5 6.5 Z" fill="var(--brand-blue)"/>
        </svg>
        +61 427 555123
      </li>
      <li>
        <svg viewBox="0 0 22 22" aria-hidden="true">
          <rect x="1.5" y="4.5" width="19" height="13" fill="none" stroke="var(--brand-blue)" stroke-width="1.6"/>
          <path d="M1.5 4.5 L11 12 L20.5 4.5 M1.5 17.5 L8.5 10.5 M20.5 17.5 L13.5 10.5" fill="none" stroke="var(--brand-blue)" stroke-width="1.4"/>
        </svg>
        xxxx@brightforge.com
      </li>
      <li>
        <svg viewBox="0 0 22 22" aria-hidden="true">
          <circle cx="11" cy="11" r="9.5" fill="var(--brand-blue)"/>
        </svg>
        xxxxxbarton
      </li>
      <li>
        <svg viewBox="0 0 22 22" aria-hidden="true">
          <circle cx="11" cy="11" r="9.5" fill="var(--brand-blue)"/>
        </svg>
        nbarton
      </li>
    </ul>
    <div class="metal-strip bottom"></div>
  </section>

</body>
</html>
```